Bidlane Display ads for Real Estate Photography

I'm looking for someone to take ideas off of my flyers and website (lensvista27.example) to create two sets of display ads. One for branding and another for specific specials (see magazine-ad-special.pdf). I would like these to be animated gifs that cycle between 2 or 3 views. Here are the dimensions for the ads:
300 x 250 – Inline Rectangle
728 x 90 – Leaderboard
160 x 600 – Wide Skyscraper
320×100 - Large Mobile Banner
I can also provide source artwork from the flyers if needed.
Target Market(s)
Realtors that sell high end luxury homes
Industry/Entity Type
Professional Photography
Requirements
Must have
- .psd source files for each size ad with screens/views on different layers to I can export as an animated gif
- display ads in the following sizes:
- 300 x 250 – Inline Rectangle
- 728 x 90 – Leaderboard
- 160 x 600 – Wide Skyscraper
- 320×100 - Large Mobile Banner
Nice to have
- 336 x 280 – Large Rectangle
- 300 x 600 – Half-Page Ad

```html
<!DOCTYPE html>
<html lang="en">
<head>
<meta charset="utf-8">
<title>LensVista Display Ads Banner Design</title>
<link rel="stylesheet" href="https://fonts.googleapis.com/css2?family=Roboto:wght@300;400;500;700&display=swap">
<style>
  :root {
    --stage: #2b221d;
    --label: #ece6df;
    --blue: #1c65ad;
    --blue-deep: #0e4a8e;
    --blue-light: #2f86d6;
    --band: #a3a8ad;
    --box: rgba(58, 58, 60, 0.86);
    --white: #ffffff;
    --url: #cfe0f2;
    --photo-dark: #5e5a55;
    --photo-mid: #a8a198;
    --photo-light: #e6e2dc;
  }
  * { margin: 0; padding: 0; box-sizing: border-box; }
  html, body { width: 1200px; height: 1200px; overflow: hidden; }
  body {
    background: var(--stage);
    font-family: "Roboto", sans-serif;
    position: relative;
  }
  .sheet-title {
    position: absolute; left: 0; right: 0; top: 76px;
    text-align: center; color: var(--label);
    font-weight: 300; font-size: 29px; letter-spacing: 0.5px;
  }
  .size-label {
    position: absolute; color: var(--label);
    font-size: 13px; font-weight: 400;
  }
  .ad {
    position: absolute; overflow: hidden;
    background: linear-gradient(160deg, var(--blue) 0%, var(--blue-deep) 100%);
  }
  .ad-art { position: absolute; inset: 0; width: 100%; height: 100%; }
  .brand {
    position: absolute; color: var(--white);
    font-weight: 700; letter-spacing: -0.5px; line-height: 1;
  }
  .headline {
    position: absolute; background: var(--box);
    color: var(--white); font-weight: 400; text-transform: uppercase;
    display: flex; align-items: center; justify-content: center; text-align: center;
  }
  .url {
    position: absolute; color: var(--url); font-weight: 400;
    display: flex; align-items: center; gap: 4px; white-space: nowrap;
  }
  .url svg { flex: none; }
  .cta {
    position: absolute; color: var(--white); font-weight: 500;
    background: linear-gradient(180deg, var(--blue-light), #1b6fc0);
    border: 1px solid #8fc3f0; border-radius: 4px;
    display: flex; align-items: center; justify-content: center; gap: 3px;
    text-transform: uppercase; white-space: nowrap;
  }
</style>
</head>
<body>

<h1 class="sheet-title">LENSVISTA DISPLAY ADS BANNER DESIGN</h1>

<!-- Leaderboard 728x90 -->
<span class="size-label" style="left:213px;top:208px">728-90</span>
<div class="ad ad-leaderboard" style="left:214px;top:237px;width:582px;height:72px">
  <svg class="ad-art" viewBox="0 0 582 72" preserveAspectRatio="none">
    <defs>
      <linearGradient id="lbPhoto" x1="0" x2="1">
        <stop offset="0" stop-color="var(--photo-dark)"/>
        <stop offset="0.5" stop-color="var(--photo-light)"/>
        <stop offset="1" stop-color="var(--photo-mid)"/>
      </linearGradient>
    </defs>
    <polygon points="93,0 470,0 430,72 92,72" fill="#eef0f2"/>
    <rect x="137" y="0" width="320" height="72" fill="url(#lbPhoto)" role="img" aria-label="Bright modern kitchen interior photograph"/>
    <polygon points="93,0 137,0 137,72 92,72 " fill="#e4e7ea"/>
    <polygon points="0,0 140,0 93,72 0,72" fill="var(--blue)"/>
    <polygon points="470,0 582,0 582,72 430,72" fill="var(--blue)"/>
  </svg>
  <div class="brand" style="left:18px;top:24px;font-size:22px">LensVista</div>
  <div class="headline" style="left:137px;top:0;width:121px;height:72px;font-size:12.5px;line-height:1.4">Grow your<br>business &amp; sell<br>more homes</div>
  <div class="url" style="right:7px;top:21px;font-size:9.5px">
    <svg width="10" height="10" viewBox="0 0 12 12"><circle cx="6" cy="6" r="5" fill="none" stroke="#8fc3f0"/><path d="M1 6h10M6 1v10M3 3h6M3 9h6" stroke="#8fc3f0" stroke-width="0.8"/></svg>lensvista27.example</div>
  <div class="cta" style="left:479px;top:42px;width:97px;height:24px;font-size:11px">Read more &raquo;</div>
</div>

<!-- Inline rectangle 300x250 -->
<span class="size-label" style="left:212px;top:344px">300-250</span>
<div class="ad ad-rect" style="left:214px;top:366px;width:240px;height:200px">
  <svg class="ad-art" viewBox="0 0 240 200" preserveAspectRatio="none">
    <defs>
      <linearGradient id="rcPhoto" x1="0" x2="1">
        <stop offset="0" stop-color="var(--photo-dark)"/>
        <stop offset="0.55" stop-color="var(--photo-light)"/>
        <stop offset="1" stop-color="var(--photo-mid)"/>
      </linearGradient>
    </defs>
    <path d="M0 46 Q120 20 240 28 L240 134 Q120 160 0 170 Z" fill="url(#rcPhoto)" role="img" aria-label="Kitchen with white cabinets and glass doors"/>
    <path d="M0 46 Q120 20 240 28" fill="none" stroke="var(--band)" stroke-width="3"/>
  </svg>
  <div class="brand" style="left:8px;top:11px;font-size:20px">LensVista</div>
  <div class="headline" style="left:7px;top:34px;width:121px;height:111px;font-size:13px;line-height:1.35">Grow your<br>business &amp; sell<br>more homes</div>
  <div class="url" style="left:12px;top:178px;font-size:10.5px">
    <svg width="11" height="11" viewBox="0 0 12 12"><circle cx="6" cy="6" r="5" fill="none" stroke="#8fc3f0"/><path d="M1 6h10M6 1v10M3 3h6M3 9h6" stroke="#8fc3f0" stroke-width="0.8"/></svg>lensvista27.example</div>
  <div class="cta" style="left:138px;top:173px;width:97px;height:24px;font-size:11.5px">Read more &raquo;</div>
</div>

<!-- Large rectangle 336x280 -->
<span class="size-label" style="left:212px;top:600px">336-280</span>
<div class="ad ad-large-rect" style="left:213px;top:622px;width:269px;height:224px">
  <svg class="ad-art" viewBox="0 0 269 224" preserveAspectRatio="none">
    <defs>
      <linearGradient id="lrPhoto" x1="0" x2="1">
        <stop offset="0" stop-color="var(--photo-dark)"/>
        <stop offset="0.55" stop-color="var(--photo-light)"/>
        <stop offset="1" stop-color="var(--photo-mid)"/>
      </linearGradient>
    </defs>
    <path d="M0 74 Q130 40 269 36 L269 158 Q130 185 0 196 Z" fill="url(#lrPhoto)" role="img" aria-label="Kitchen with white cabinets and dark wine fridge"/>
    <path d="M0 74 Q130 40 269 36" fill="none" stroke="var(--band)" stroke-width="3"/>
  </svg>
  <div class="brand" style="left:8px;top:13px;font-size:24px">LensVista</div>
  <div class="headline" style="left:6px;top:45px;width:120px;height:105px;font-size:13px;line-height:1.35">Grow your<br>business &amp; sell<br>more homes</div>
  <div class="url" style="left:12px;top:203px;font-size:10.5px">
    <svg width="11" height="11" viewBox="0 0 12 12"><circle cx="6" cy="6" r="5" fill="none" stroke="#8fc3f0"/><path d="M1 6h10M6 1v10M3 3h6M3 9h6" stroke="#8fc3f0" stroke-width="0.8"/></svg>lensvista27.example</div>
  <div class="cta" style="left:166px;top:195px;width:97px;height:25px;font-size:11.5px">Read more &raquo;</div>
</div>

<!-- Wide skyscraper 160x600 -->
<span class="size-label" style="left:532px;top:344px">160-600</span>
<div class="ad ad-skyscraper" style="left:531px;top:366px;width:128px;height:480px">
  <svg class="ad-art" viewBox="0 0 128 480" preserveAspectRatio="none">
    <defs>
      <linearGradient id="skPhoto" x1="0" x2="0" y1="0" y2="1">
        <stop offset="0" stop-color="var(--photo-mid)"/>
        <stop offset="0.5" stop-color="var(--photo-light)"/>
        <stop offset="1" stop-color="var(--photo-mid)"/>
      </linearGradient>
    </defs>
    <path d="M0 102 Q64 80 128 78 L128 366 Q64 385 0 398 Z" fill="url(#skPhoto)" role="img" aria-label="Kitchen with steel fridge and granite counter"/>
    <path d="M0 102 Q64 80 128 78" fill="none" stroke="var(--band)" stroke-width="3"/>
  </svg>
  <div class="brand" style="left:9px;top:32px;font-size:24px">LensVista</div>
  <div class="headline" style="left:2px;top:106px;width:123px;height:72px;font-size:12px;line-height:1.45">Grow your<br>business &amp; sell<br>more homes</div>
  <div class="url" style="left:0;right:0;justify-content:center;top:419px;font-size:9.5px">
    <svg width="10" height="10" viewBox="0 0 12 12"><circle cx="6" cy="6" r="5" fill="none" stroke="#8fc3f0"/><path d="M1 6h10M6 1v10M3 3h6M3 9h6" stroke="#8fc3f0" stroke-width="0.8"/></svg>lensvista27.example</div>
  <div class="cta" style="left:14px;top:443px;width:99px;height:25px;font-size:11.5px">Read more &raquo;</div>
</div>

<!-- Half-page 300x600 -->
<span class="size-label" style="left:704px;top:344px">300-600</span>
<div class="ad ad-half-page" style="left:706px;top:366px;width:240px;height:480px">
  <svg class="ad-art" viewBox="0 0 240 480" preserveAspectRatio="none">
    <defs>
      <linearGradient id="hpPhoto" x1="0" x2="1" y1="0" y2="1">
        <stop offset="0" stop-color="var(--photo-mid)"/>
        <stop offset="0.5" stop-color="var(--photo-light)"/>
        <stop offset="1" stop-color="#cfc8be"/>
      </linearGradient>
    </defs>
    <path d="M0 138 Q120 90 240 86 L240 358 Q120 395 0 402 Z" fill="url(#hpPhoto)" role="img" aria-label="White kitchen with tiled backsplash and coffee maker"/>
    <path d="M0 138 Q120 90 240 86" fill="none" stroke="var(--band)" stroke-width="3"/>
  </svg>
  <div class="brand" style="left:0;right:0;top:32px;text-align:center;font-size:44px">LensVista</div>
  <div class="headline" style="left:11px;top:114px;width:217px;height:116px;font-size:20px;line-height:1.35">Grow your<br>business &amp; sell<br>more homes</div>
  <div class="url" style="left:0;right:0;top:416px;justify-content:center;font-size:14px">
    <svg width="15" height="15" viewBox="0 0 12 12"><circle cx="6" cy="6" r="5" fill="none" stroke="#8fc3f0"/><path d="M1 6h10M6 1v10M3 3h6M3 9h6" stroke="#8fc3f0" stroke-width="0.8"/></svg>lensvista27.example</div>
  <div class="cta" style="left:71px;top:445px;width:99px;height:25px;font-size:11.5px">Read more &raquo;</div>
</div>

<!-- Large mobile banner 320x100 -->
<span class="size-label" style="left:212px;top:880px">320×100</span>
<div class="ad ad-mobile" style="left:213px;top:907px;width:256px;height:80px">
  <svg class="ad-art" viewBox="0 0 256 80" preserveAspectRatio="none">
    <defs>
      <linearGradient id="mbPhoto" x1="0" x2="1">
        <stop offset="0" stop-color="var(--photo-dark)"/>
        <stop offset="0.5" stop-color="var(--photo-light)"/>
        <stop offset="1" stop-color="var(--photo-dark)"/>
      </linearGradient>
    </defs>
    <polygon points="70,0 215,0 150,80 20,80" fill="url(#mbPhoto)" role="img" aria-label="Kitchen interior photograph"/>
    <polygon points="0,0 70,0 18,80 0,80" fill="var(--blue)"/>
    <polygon points="215,0 256,0 256,80 150,80" fill="var(--blue)"/>
  </svg>
  <div class="brand" style="left:6px;top:11px;font-size:18px">LensVista</div>
  <div class="headline" style="left:34px;top:34px;width:110px;height:46px;font-size:8.5px;line-height:1.35">Grow your<br>business &amp; sell<br>more homes</div>
  <div class="url" style="right:3px;top:28px;flex-direction:column;gap:2px;font-size:7px">
    <svg width="10" height="10" viewBox="0 0 12 12"><circle cx="6" cy="6" r="5" fill="none" stroke="#8fc3f0"/><path d="M1 6h10M6 1v10M3 3h6M3 9h6" stroke="#8fc3f0" stroke-width="0.8"/></svg>lensvista27.example</div>
  <div class="cta" style="left:187px;top:57px;width:66px;height:20px;font-size:8px">Read more &raquo;</div>
</div>

</body>
</html>
```